The Harvest Ledger App - Modernization & Graphics User Interface Friendliness Updates

We are Harvest Ledger, and we want to bring a new branding look and graphical user interface to the Harvest Ledger App. The app is a quick reference encyclopedia for all things produce. Boasting articles on over 2,000 produce items, with information ranging from taste and application to geographical and cultural significance. Included in its features are over 10 thousand recipes, and the Harvest Ledger App Crop Bazaar – a global initiative to connect farmer, customer, and chef in one sustainable and easy to use application. The design needs to bring a greater sense of social connection – encouraging the user to participate in the 'Crop Bazaar' experience voluntarily. The design should reflect a sense of authority reflecting the authenticity and reliability of the provided information, it's writing, and its sources. Download the App here: hvldg.example/get

Target Market(s)

Women and Men between ages 21-55.

Industry/Entity Type

Education

Font styles to use
Serif
Sans Serif

Colors

Designer to choose colors to be used in the design.

Requirements
Must have
• An updated user interface, the intuitive usability of the app is currently non-existent. We are looking to reflect as the authority on produce. The app design must reflect a professional, user-friendly, up-to-date, and trustworthy feel.
Nice to have
• To incorporate the social draw of the Crop Bazaar we would like to include on the home page "Social Bubbles" (think Pictaloo stories) which updates with shared photos of produce and their location.
Should not have
• An overly complicated theme, distracting or unprofessional colors, and images.

```html
<!DOCTYPE html>
<html lang="en">
<head>
<meta charset="utf-8">
<title>Harvest Ledger App — Screens</title>
<link href="https://fonts.googleapis.com/css2?family=Montserrat:wght@400;600;700&family=Nunito:wght@600;700;800&display=swap" rel="stylesheet">
<style>
:root{
  --page:#e9e4da;
  --screen:#f4f4f5;
  --card:#ffffff;
  --ink:#1d1d1f;
  --muted:#9a9a9e;
  --faint:#c9c9cc;
  --icon:#c6c6ca;
  --badge:#f25c5c;
}
*{box-sizing:border-box;margin:0;padding:0}
html,body{width:1200px;height:1025px;overflow:hidden;background:var(--page)}
body{position:relative;font-family:"Montserrat",sans-serif;color:var(--ink)}
.screen{position:absolute;top:116px;width:450px;height:792px;background:var(--screen);overflow:hidden;border-radius:4px;box-shadow:0 10px 30px rgba(80,70,50,.18)}
.screen--feed{left:130px}
.screen--categories{left:620px}

/* feed */
.feed{position:absolute;left:14px;top:14px;right:15px;bottom:60px;display:flex;gap:9px;overflow:hidden}
.feed__col{flex:1;display:flex;flex-direction:column;gap:14px}
.post{background:var(--card);flex-shrink:0}
.post__photo{display:block;width:100%}
.post__body{padding:12px 14px 14px}
.post__title{font-size:11px;font-weight:700;text-transform:uppercase;letter-spacing:.1px}
.post__market{font-size:10px;color:var(--muted);letter-spacing:.8px;margin-top:7px}
.post__blurb{font-size:6.5px;color:var(--faint);line-height:1.4;margin-top:9px}
.post__author{display:flex;align-items:center;gap:10px;margin-top:16px;font-size:7px;color:var(--muted)}
.avatar{width:14px;height:14px;border-radius:50%;background:#d8c3b4}

/* categories */
.status{height:32px;display:flex;align-items:center;justify-content:space-between;padding:0 14px;font-family:"Nunito",sans-serif;font-weight:600;font-size:14px;background:var(--card)}
.status__left,.status__right{display:flex;align-items:center;gap:5px;width:130px}
.status__right{justify-content:flex-end}
.navbar{height:68px;background:var(--card);display:flex;align-items:center;justify-content:space-between;padding:0 22px 0 30px}
.navbar__title{font-family:"Nunito",sans-serif;font-weight:700;font-size:14px}
.grid{display:grid;grid-template-columns:202px 202px;gap:20px 13px;padding:26px 16px 0}
.category{position:relative;height:177px;background:var(--card);border-radius:3px}
.category__photo{position:absolute;left:18px;right:18px;top:22px;height:86px;border-radius:40%}
.category__label{position:absolute;left:22px;right:20px;bottom:16px;display:flex;justify-content:space-between;align-items:center;font-family:"Nunito",sans-serif;font-weight:800;font-size:14px}
.badge{position:absolute;right:16px;top:11px;width:30px;height:30px;border-radius:50%;background:var(--badge);color:#fff;font-family:"Nunito",sans-serif;font-weight:700;font-size:12px;display:flex;align-items:center;justify-content:center}

/* tab bar */
.tabbar{position:absolute;left:0;right:0;bottom:0;height:60px;background:var(--card);display:flex;justify-content:space-around;align-items:center;padding:0 20px}
</style>
</head>
<body>

<section class="screen screen--feed">
  <div class="feed">
    <div class="feed__col">
      <article class="post">
        <div class="post__photo" role="img" aria-label="Bunch of fresh green basil leaves" style="height:186px;background:linear-gradient(150deg,#9cc46a,#4e8a2c 55%,#2f5f1c)"></div>
        <div class="post__body">
          <h2 class="post__title">Herbs Basil</h2>
          <p class="post__market">Bayview Growers Market</p>
          <p class="post__blurb">Fresh leaves picked at dawn, sold by the bunch near the east gate. Best used within two days.</p>
          <p class="post__author"><span class="avatar"></span>Nora Fielding</p>
        </div>
      </article>
      <article class="post">
        <div class="post__photo" role="img" aria-label="Pile of long purple aubergines" style="height:186px;background:linear-gradient(160deg,#8a6b9c,#4a2f5c 50%,#2b1a38)"></div>
        <div class="post__body">
          <h2 class="post__title">Aubergines Blue</h2>
          <p class="post__market">Pell's Open Market</p>
          <p class="post__blurb">Glossy slender fruit grown in open rows, mild and sweet when roasted over an open flame.</p>
          <p class="post__author"><span class="avatar"></span>Owen Marsh</p>
        </div>
      </article>
      <article class="post">
        <div class="post__photo" role="img" aria-label="Red tomatoes in a basket among leaves" style="height:120px;background:linear-gradient(120deg,#4f8a3a,#7a9a4a 40%,#d8322c 70%,#2e6f96)"></div>
      </article>
    </div>
    <div class="feed__col">
      <article class="post">
        <div class="post__photo" role="img" aria-label="Bowl of small red chile peppers" style="height:166px;background:linear-gradient(140deg,#c8271c,#e3452a 50%,#9aa7ad)"></div>
        <div class="post__body">
          <h2 class="post__title">Pepper Chile de Agua</h2>
          <p class="post__market">Alder Creek Farms</p>
          <p class="post__author"><span class="avatar"></span>Tess Varga</p>
        </div>
      </article>
      <article class="post">
        <div class="post__photo" role="img" aria-label="Bunches of red and white radishes with green tops" style="height:134px;background:linear-gradient(180deg,#4f7f36,#7ea45a 35%,#d2366a 65%,#8a8e8c)"></div>
        <div class="post__body">
          <h2 class="post__title">Radish</h2>
          <p class="post__market">Ridgeline Farm Market</p>
          <p class="post__author"><span class="avatar"></span>Iris Calloway</p>
        </div>
      </article>
      <article class="post">
        <div class="post__photo" role="img" aria-label="Small bumpy cucumbers with dill flowers" style="height:186px;background:linear-gradient(150deg,#c9b25a,#5e9a3a 35%,#3c7a2a 70%,#e3e3d8)"></div>
      </article>
    </div>
  </div>
  <nav class="tabbar" aria-label="Main">
    <svg width="28" height="32" viewBox="0 0 28 32" fill="var(--icon)"><path d="M14 9c-3-2-11-2-11 8 0 8 5 14 8 14 1.5 0 2-1 3-1s1.5 1 3 1c3 0 8-6 8-14 0-10-8-10-11-8z"/><rect x="13" y="2" width="2" height="7" rx="1"/></svg>
    <svg width="24" height="32" viewBox="0 0 24 32"><rect x="1" y="1" width="22" height="30" rx="1" fill="var(--icon)"/><path d="M7 10l10 12M17 10L7 22" stroke="#fff" stroke-width="2"/></svg>
    <svg width="40" height="24" viewBox="0 0 40 24"><path d="M2 12C10 2 30 2 38 12 30 22 10 22 2 12z" fill="none" stroke="var(--icon)" stroke-width="3"/><circle cx="20" cy="12" r="6" fill="var(--icon)"/></svg>
    <svg width="32" height="26" viewBox="0 0 32 26"><rect x="1.5" y="1.5" width="29" height="23" fill="none" stroke="var(--icon)" stroke-width="3"/><path d="M4 22l8-9 6 6 4-4 6 7z" fill="var(--icon)"/><circle cx="23" cy="8" r="2.5" fill="var(--icon)"/></svg>
    <svg width="28" height="28" viewBox="0 0 28 28"><g fill="var(--icon)"><circle cx="14" cy="14" r="9"/><g stroke="var(--icon)" stroke-width="5"><path d="M14 1v26M1 14h26M4.8 4.8l18.4 18.4M23.2 4.8L4.8 23.2"/></g></g><circle cx="14" cy="14" r="4" fill="#fff"/></svg>
  </nav>
</section>

<section class="screen screen--categories">
  <header class="status">
    <span class="status__left">●●●○○ LARK
      <svg width="14" height="11" viewBox="0 0 14 11"><path d="M1 4a9 9 0 0112 0M3 6.5a6 6 0 018 0M5 9a3 3 0 014 0" fill="none" stroke="var(--ink)" stroke-width="1.6"/></svg>
    </span>
    <span>4:21 PM</span>
    <span class="status__right">100%
      <svg width="30" height="12" viewBox="0 0 30 12"><rect x=".5" y=".5" width="26" height="11" rx="2" fill="none" stroke="var(--ink)"/><rect x="2" y="2" width="23" height="8" rx="1" fill="var(--ink)"/><rect x="27.5" y="4" width="2" height="4" fill="var(--ink)"/></svg>
    </span>
  </header>
  <div class="navbar">
    <svg width="22" height="22" viewBox="0 0 22 22"><circle cx="9" cy="9" r="6.5" fill="none" stroke="var(--ink)" stroke-width="2.4"/><path d="M14 14l6 6" stroke="var(--ink)" stroke-width="2.6" stroke-linecap="round"/></svg>
    <h1 class="navbar__title">Categories</h1>
    <svg width="22" height="18" viewBox="0 0 22 18" fill="var(--ink)"><rect y="1" width="22" height="3"/><rect y="7.5" width="22" height="3"/><rect y="14" width="22" height="3"/></svg>
  </div>
  <div class="grid">
    <a class="category"><div class="category__photo" role="img" aria-label="Assorted fruit with bananas, apples and citrus" style="background:radial-gradient(closest-side,#f0b72a,#e6572c 55%,rgba(255,255,255,0))"></div><span class="category__label">All Fruit <svg width="8" height="13" viewBox="0 0 8 13"><path d="M1 1l5.5 5.5L1 12" fill="none" stroke="var(--ink)" stroke-width="1.5"/></svg></span></a>
    <a class="category"><div class="category__photo" role="img" aria-label="Assorted vegetables with peppers, corn and cauliflower" style="background:radial-gradient(closest-side,#e9c93a,#5c9e33 55%,rgba(255,255,255,0))"></div><span class="category__label">All Vegetables <svg width="8" height="13" viewBox="0 0 8 13"><path d="M1 1l5.5 5.5L1 12" fill="none" stroke="var(--ink)" stroke-width="1.5"/></svg></span></a>
    <a class="category"><div class="category__photo" role="img" aria-label="Heap of mixed fresh produce" style="background:radial-gradient(closest-side,#d9452c,#4f8e2e 60%,rgba(255,255,255,0))"></div><span class="badge">25</span><span class="category__label">Spotted Produce <svg width="8" height="13" viewBox="0 0 8 13"><path d="M1 1l5.5 5.5L1 12" fill="none" stroke="var(--ink)" stroke-width="1.5"/></svg></span></a>
    <a class="category"><div class="category__photo" role="img" aria-label="Assorted foraged mushrooms" style="background:radial-gradient(closest-side,#c9a88a,#7a5238 60%,rgba(255,255,255,0))"></div><span class="category__label">Foraged <svg width="8" height="13" viewBox="0 0 8 13"><path d="M1 1l5.5 5.5L1 12" fill="none" stroke="var(--ink)" stroke-width="1.5"/></svg></span></a>
    <a class="category"><div class="category__photo" role="img" aria-label="Asian greens, herbs and root vegetables" style="background:radial-gradient(closest-side,#6f9e4a,#3f7a34 55%,rgba(255,255,255,0))"></div><span class="category__label">Asian Specialties <svg width="8" height="13" viewBox="0 0 8 13"><path d="M1 1l5.5 5.5L1 12" fill="none" stroke="var(--ink)" stroke-width="1.5"/></svg></span></a>
    <a class="category"><div class="category__photo" role="img" aria-label="Bunch of leafy Indian greens" style="background:radial-gradient(closest-side,#3f7a2e,#5d9a3e 50%,rgba(255,255,255,0))"></div><span class="category__label">Indian Specialties <svg width="8" height="13" viewBox="0 0 8 13"><path d="M1 1l5.5 5.5L1 12" fill="none" stroke="var(--ink)" stroke-width="1.5"/></svg></span></a>
  </div>
  <nav class="tabbar" aria-label="Main">
    <svg width="28" height="32" viewBox="0 0 28 32" fill="var(--icon)"><path d="M14 9c-3-2-11-2-11 8 0 8 5 14 8 14 1.5 0 2-1 3-1s1.5 1 3 1c3 0 8-6 8-14 0-10-8-10-11-8z"/><rect x="13" y="2" width="2" height="7" rx="1"/></svg>
    <svg width="24" height="32" viewBox="0 0 24 32"><rect x="1" y="1" width="22" height="30" rx="1" fill="var(--icon)"/><path d="M7 10l10 12M17 10L7 22" stroke="#fff" stroke-width="2"/></svg>
    <svg width="40" height="24" viewBox="0 0 40 24"><path d="M2 12C10 2 30 2 38 12 30 22 10 22 2 12z" fill="none" stroke="var(--icon)" stroke-width="3"/><circle cx="20" cy="12" r="6" fill="var(--icon)"/></svg>
    <svg width="32" height="26" viewBox="0 0 32 26"><rect x="1.5" y="1.5" width="29" height="23" fill="none" stroke="var(--icon)" stroke-width="3"/><path d="M4 22l8-9 6 6 4-4 6 7z" fill="var(--icon)"/><circle cx="23" cy="8" r="2.5" fill="var(--icon)"/></svg>
    <svg width="28" height="28" viewBox="0 0 28 28"><g fill="var(--icon)"><circle cx="14" cy="14" r="9"/><g stroke="var(--icon)" stroke-width="5"><path d="M14 1v26M1 14h26M4.8 4.8l18.4 18.4M23.2 4.8L4.8 23.2"/></g></g><circle cx="14" cy="14" r="4" fill="#fff"/></svg>
  </nav>
</section>

</body>
</html>
```